Bright Leaf Company Needs New Packaging Design

We need a design to print directly on our stand up zip pouches, 6x9x3 in., to replace the labels we were applying on generic matte black pouches.

We'd like to keep the current color theme of matte black + [Flavor Color] (in this case, fushia) to communicate the idea of modern, luxury brand (please see velcorra coffee brand) and stay somewhat close to the current label so our product will be recognized by actual customers. Other flavors will be a declination of the same layout, matte black + [flavor color]. Colors used should be vibrant, eye catching, to stand out from competition.

We also want to display the actual tea blend picture on the packaging so the consumer can see how beautiful the tea is. The font size for Amber Orchard Meadow should be big enough so it's readable when the product is seen in thumbnail format.

The front should have a seal/stamp close to a top corner with a big "100% Freshness Guarantee",

The company logo "The Lumo Company" should be present on the front in a prominent spot. It's provided in the zip file from old label.

We need to display the net weight (4oz / 113g) and number of servings (makes 60 cups). Please refer to old label.

On the back side we need a space for the UPC barcode at the bottom, the company address, a space for the brand's story/mission, steeping instructions with icons (see current label), ingredients and another section featuring our other products. All fonts should be 10pt or bigger.

Artwork of the current label current label is available here
https://files.zentrovault.example/folders/7Qx2mRpL4vNa8sKd1TyHwBcE?resourcekey=0-Fk39LwQpz8RnVt2XyMbCaJ&usp=sharing

Target Market(s)

USA market, Women ages 25-45, young & young at heart, trendy, health conscious, luxury

Industry/Entity Type

Premium Loose Leaf Tea

Font styles to use
Other font styles liked:
• fonts provided in zip file

Colors
E54698
E96AAD
F1A4CE
F9D9EA
FCEFF6

Requirements
Must have
• See description
Should not have
• Asian look and feel

```html
<!DOCTYPE html>
<html lang="en">
<head>
<meta charset="utf-8">
<title>The Lumo Company – Amber Orchard Meadow Tea Pouch</title>
<link href="https://fonts.googleapis.com/css2?family=Lora:ital,wght@0,400;0,500;0,600;1,400;1,500&family=Montserrat:wght@400;500;600;700;800&display=swap" rel="stylesheet">
<style>
  :root{
    --ink:#2b2b2b;
    --pouch:#121212;
    --pouch-edge:#1f1f1f;
    --flavor:#e54698;
    --flavor-mid:#e96aad;
    --flavor-soft:#f1a4ce;
    --flavor-pale:#f9d9ea;
    --white:#ffffff;
    --muted:#cfcfcf;
    --bg:#ffffff;
    --blend-a:#d9a93a;
    --blend-b:#b9546a;
    --blend-c:#8f8a7a;
  }
  *{box-sizing:border-box;margin:0;padding:0}
  html,body{width:1200px;height:900px;overflow:hidden;background:var(--bg)}
  .canvas{position:relative;width:1200px;height:900px;font-family:"Lora",serif;color:var(--ink)}

  /* Brand wordmark */
  .brand-mark{position:absolute;left:0;top:58px;width:1200px;text-align:center;font-family:"Lora",serif;font-weight:500;color:var(--ink);line-height:1}
  .brand-mark .line-small{display:block;font-size:34px}
  .brand-mark .line-big{display:block;font-size:92px;margin-top:6px}
  .brand-mark .line-small.bottom{margin-top:6px}
  .brand-mark .dot{position:absolute;left:660px;top:0;width:26px;height:26px;border-radius:50%;background:var(--flavor)}

  /* Pouches */
  .pouch{position:absolute;top:310px;width:340px;height:535px;background:var(--pouch);border-radius:14px 14px 10px 10px;overflow:hidden;color:var(--white)}
  .pouch-front{left:240px}
  .pouch-back{left:617px}

  .organic-seal{position:absolute;right:14px;top:22px;width:66px;height:66px;border:1.5px solid var(--white);border-radius:50%;display:flex;flex-direction:column;align-items:center;justify-content:center;font-family:"Montserrat",sans-serif;font-size:15px;line-height:1.05;transform:rotate(-12deg)}

  /* Front */
  .brand-tab{position:absolute;left:125px;top:0;width:86px;height:115px;background:var(--flavor);display:flex;flex-direction:column;align-items:center;justify-content:center;font-family:"Lora",serif;font-weight:500;color:var(--white);line-height:1}
  .brand-tab .s{font-size:11px}
  .brand-tab .b{font-size:25px;margin:3px 0}
  .product-title{position:absolute;left:0;top:122px;width:340px;text-align:center;font-family:"Montserrat",sans-serif;font-weight:600;font-size:30px;line-height:1.08;color:var(--flavor);letter-spacing:.2px}
  .product-tagline{position:absolute;left:0;top:198px;width:340px;text-align:center;font-family:"Lora",serif;font-style:italic;font-size:19px;color:var(--white)}
  .front-art{position:absolute;left:0;top:220px;width:340px;height:315px}
  .servings{position:absolute;left:12px;bottom:22px;font-family:"Montserrat",sans-serif;font-weight:800;color:var(--pouch);text-align:center;line-height:1}
  .servings .sm{display:block;font-size:10px}
  .servings .num{display:block;font-size:26px}
  .loose-leaf{position:absolute;left:0;bottom:12px;width:340px;text-align:center;font-family:"Montserrat",sans-serif;font-weight:500;font-size:12px;letter-spacing:.6px;color:var(--white)}
  .net-weight{position:absolute;right:14px;bottom:20px;font-family:"Montserrat",sans-serif;font-weight:600;font-size:9px;color:var(--pouch);line-height:1.2}
  .net-weight b{font-size:12px;font-weight:600}

  /* Back */
  .back-brand{position:absolute;left:0;top:22px;width:340px;text-align:center;font-family:"Lora",serif;font-weight:500;color:var(--white);line-height:1}
  .back-brand .s{display:block;font-size:16px}
  .back-brand .b{display:block;font-size:42px;margin:2px 0}
  .back-heading{position:absolute;left:0;top:132px;width:340px;text-align:center;font-style:italic;font-size:12.5px;line-height:1.35}
  .ingredients{position:absolute;left:22px;top:170px;width:296px;text-align:center;font-size:7.5px;line-height:1.45;color:var(--muted)}
  .steeping{position:absolute;left:40px;top:192px;width:260px;display:flex;justify-content:space-between}
  .steep-item{width:80px;text-align:center;font-size:6.5px;line-height:1.3;color:var(--muted)}
  .steep-item svg{display:block;margin:0 auto 6px}
  .divider{position:absolute;left:68px;width:204px;height:1.5px;background:var(--flavor)}
  .divider.one{top:258px}
  .section-title{position:absolute;left:0;width:340px;text-align:center;font-style:italic;font-size:13px;color:var(--white)}
  .section-title.sellers{top:266px}
  .section-title.story{top:394px}
  .sellers-row{position:absolute;left:52px;top:289px;width:240px;display:flex;justify-content:space-between}
  .seller{width:70px;text-align:center}
  .seller-card{width:66px;height:74px;background:var(--white);border-radius:3px;margin:0 auto;padding:6px 8px}
  .seller-thumb{width:100%;height:100%;border-radius:2px;background:linear-gradient(160deg,var(--pouch) 0 45%,var(--flavor) 45% 58%,var(--blend-a) 58% 80%,var(--blend-b) 80%)}
  .seller-name{margin-top:4px;font-size:8.5px;color:var(--white);white-space:nowrap}
  .story-text{position:absolute;left:24px;top:413px;width:292px;font-size:8px;line-height:1.25;color:var(--muted);text-align:justify}
  .caffeine-seal{position:absolute;left:26px;bottom:12px;width:46px;height:46px;border-radius:50%;background:var(--white);color:var(--pouch);font-family:"Montserrat",sans-serif;font-weight:600;font-size:8.5px;line-height:1.1;display:flex;align-items:center;justify-content:center;text-align:center}
  .address{position:absolute;left:100px;top:480px;width:140px;text-align:center;font-family:"Montserrat",sans-serif;font-size:5.5px;line-height:1.3;color:var(--white)}
  .best-by{position:absolute;left:104px;top:503px;width:132px;height:28px;background:var(--white);color:var(--pouch);text-align:center;font-family:"Montserrat",sans-serif;line-height:1.15;padding-top:2px}
  .best-by b{display:block;font-size:8.5px;font-weight:700}
  .best-by span{display:block;font-size:4.6px;font-weight:600}
  .upc-box{position:absolute;right:30px;bottom:12px;width:62px;height:40px;background:var(--white);color:var(--pouch);font-family:"Montserrat",sans-serif;font-weight:700;font-size:16px;display:flex;align-items:center;justify-content:center}
</style>
</head>
<body>
<div class="canvas">

  <div class="brand-mark" aria-label="The Lumo Company">
    <span class="line-small">The</span>
    <span class="line-big">Lumo</span>
    <span class="line-small bottom">company</span>
    <span class="dot"></span>
  </div>

  <!-- Front panel -->
  <section class="pouch pouch-front">
    <div class="brand-tab"><span class="s">The</span><span class="b">Lumo</span><span class="s">company</span></div>
    <div class="organic-seal"><span>100%</span><span>Organic</span></div>
    <h1 class="product-title">AMBER ORCHARD<br>MEADOW TEA</h1>
    <p class="product-tagline">Calming &amp; Soothing</p>
    <svg class="front-art" viewBox="0 0 340 315" xmlns="http://www.w3.org/2000/svg">
      <defs>
        <linearGradient id="blend" x1="0" y1="0" x2="1" y2="1">
          <stop offset="0" stop-color="var(--blend-b)"/>
          <stop offset=".45" stop-color="var(--blend-a)"/>
          <stop offset="1" stop-color="var(--blend-c)"/>
        </linearGradient>
      </defs>
      <path d="M0 95 C 110 30, 240 20, 340 18 L340 315 L0 315 Z" fill="var(--flavor)"/>
      <path d="M14 300 C 10 170, 130 70, 322 38 C 330 170, 260 300, 14 300 Z" fill="var(--white)"/>
      <path d="M0 285 L340 285 L340 315 L0 315 Z" fill="var(--flavor)"/>
      <path d="M0 235 C 20 250, 60 260, 90 270 L90 285 L0 285 Z" fill="var(--white)"/>
      <path d="M250 285 C 280 275, 310 262, 340 248 L340 285 Z" fill="var(--white)"/>
      <path d="M32 270 C 30 165, 140 82, 310 55 C 312 165, 240 270, 32 270 Z" fill="url(#blend)" role="img" aria-label="Photo of the loose leaf tea blend: dried chamomile flowers, rose petals and lavender buds"/>
    </svg>
    <div class="servings"><span class="sm">MAKES</span><span class="num">60</span><span class="sm">CUPS</span></div>
    <div class="loose-leaf">LOOSE LEAF</div>
    <div class="net-weight">Net Weight<br><b>4</b> oz. <b>113</b> g</div>
  </section>

  <!-- Back panel -->
  <section class="pouch pouch-back">
    <div class="back-brand"><span class="s">The</span><span class="b">Lumo</span><span class="s">company</span></div>
    <div class="organic-seal"><span>100%</span><span>Organic</span></div>
    <p class="back-heading">Calming Loose Leaf Herbal Tea<br>Made With Superior Quality Ingredients</p>
    <p class="ingredients">Organic chamomile flowers, organic rose petals, organic rose buds,<br>organic lavender flower, organic rosehips</p>

    <div class="steeping">
      <div class="steep-item">
        <svg width="16" height="16" viewBox="0 0 16 16"><circle cx="8" cy="8" r="7" fill="none" stroke="var(--muted)" stroke-width="1"/><path d="M8 3.5 V8 L11 10" fill="none" stroke="var(--muted)" stroke-width="1"/></svg>
        Steeping Time<br>5-7 Mins
      </div>
      <div class="steep-item">
        <svg width="12" height="22" viewBox="0 0 12 22"><path d="M4 2 a2 2 0 0 1 4 0 V14 a3.5 3.5 0 1 1 -4 0 Z" fill="none" stroke="var(--muted)" stroke-width="1"/><circle cx="6" cy="17" r="1.8" fill="var(--muted)"/></svg>
        Temperature<br>206° F / 95° C
      </div>
      <div class="steep-item">
        <svg width="10" height="22" viewBox="0 0 10 22"><ellipse cx="5" cy="5" rx="3.8" ry="4.3" fill="none" stroke="var(--muted)" stroke-width="1"/><path d="M5 9.3 V21" stroke="var(--muted)" stroke-width="1"/></svg>
        Qty per Cup<br>1-2 Heaping tsp
      </div>
    </div>

    <div class="divider one"></div>
    <h2 class="section-title sellers">Try Our Other Best Sellers</h2>
    <div class="sellers-row">
      <div class="seller"><div class="seller-card"><div class="seller-thumb" role="img" aria-label="Milk Oolong Tea pouch"></div></div><p class="seller-name">Milk Oolong Tea</p></div>
      <div class="seller"><div class="seller-card"><div class="seller-thumb" role="img" aria-label="Rooibos Tea pouch"></div></div><p class="seller-name">Rooibos Tea</p></div>
      <div class="seller"><div class="seller-card"><div class="seller-thumb" role="img" aria-label="Peppermint Tea pouch"></div></div><p class="seller-name">Peppermint Tea</p></div>
    </div>

    <h2 class="section-title story">Our Story... A Tradition Of Excellence</h2>
    <p class="story-text">Lorem ipsum dolor sit amet, consectetuer adipiscing elit, sed diam nonummy nibh euismod tincidunt ut laoreet dolore magna aliquam erat volutpat. Ut wisi enim ad minim veniam, quis nostrud exerci tation ullamcorper suscipit lobortis nisl ut aliquip</p>

    <div class="caffeine-seal">Caffeine<br>Free</div>
    <p class="address">The Lumo Company LLC<br>418 Marigold Ln #1207<br>Dover, DE, USA 19901</p>
    <div class="best-by"><b>BEST BY DEC 31 2025</b><span>LOT# LC0211025</span><span>STORE IN A PLACE AS COOL AS YOU</span></div>
    <div class="upc-box">UPC</div>
  </section>

</div>
</body>
</html>
```